Redesign of page from emergency manual

Please redesign this PDF to look better. Please don't include any stock photos. It must be legible. Making some words bold is probably a good idea.

Here are some things I like :

https://tarrowbooks.com.au/collections/frontpage/products/the-plk-v2-ebook

https://img-cd.vostramediafiles.com/qa-ejkwPLOTYY_SuCKbZNu411Qwgjv8YssPxEdzXN93hDkSRjLXK8WmfgbmrJW4ZZ3yUPK=w1052-h592-rw

```html
<!DOCTYPE html>
<html lang="en">
<head>
<meta charset="utf-8">
<title>Hypertension, Acute</title>
<link rel="stylesheet" href="https://fonts.googleapis.com/css2?family=Figtree:wght@400;500;700;800&display=swap">
<style>
  :root {
    --backdrop: #bfbfbf;
    --page: #ffffff;
    --ink: #2b2b2b;
    --grad-start: #0f98c8;
    --grad-mid: #4f7fcc;
    --grad-end: #9a66c8;
    --purple: #9966c8;
    --blue-head: #4a90d9;
    --blue-1: #50a4e5;
    --blue-2: #58b3ec;
    --blue-3: #5fc1f1;
    --cyan-row: #c9f0fb;
    --lavender-row: #efe1fc;
    --dot-blue: #3f8fd6;
    --dot-purple: #9a66c8;
  }
  * { box-sizing: border-box; margin: 0; padding: 0; }
  html, body { width: 1200px; height: 1200px; overflow: hidden; }
  body {
    background: var(--backdrop);
    font-family: "Figtree", sans-serif;
    color: var(--ink);
    position: relative;
  }
  .page {
    position: absolute; left: 283px; top: 35px;
    width: 635px; height: 1130px;
    background: var(--page);
  }
  .banner {
    position: absolute; left: 0; top: 0; width: 100%; height: 146px;
    background: linear-gradient(90deg, var(--grad-start), var(--grad-mid) 50%, var(--grad-end));
    color: #fff; text-align: center;
  }
  .banner h1 {
    position: absolute; left: 0; right: 0; top: 26px;
    font-size: 45px; font-weight: 800; letter-spacing: -0.3px; line-height: 1;
  }
  .banner p {
    position: absolute; left: 0; right: 0; top: 81px;
    font-size: 17.5px; line-height: 21px; font-weight: 400;
  }
  .block { position: absolute; font-size: 15px; line-height: 17.7px; }
  .intro { left: 38px; top: 167px; width: 560px; }
  .bullets { list-style: none; }
  .bullets li { position: relative; padding-left: 17px; }
  .bullets li::before {
    content: ""; position: absolute; left: 0; top: 5px;
    width: 7px; height: 7px; border-radius: 50%;
    background: var(--dot-blue); box-shadow: 0 0 0 1.5px #cfe4f7;
  }
  .bullets.purple li::before { background: var(--dot-purple); box-shadow: 0 0 0 1.5px #e6d7f5; }
  .checks { left: 38px; top: 219px; width: 230px; }
  .checks li { position: absolute; left: 0; width: 240px; }
  .range {
    position: absolute; left: 285px; top: 221px; width: 310px;
    border-collapse: collapse; color: #fff; font-size: 15px;
  }
  .range th.title {
    background: var(--purple); height: 33px; text-align: left;
    padding-left: 21px; font-weight: 700; font-size: 14.5px;
  }
  .range td { height: 33px; padding-left: 26px; border: 1px solid rgba(255,255,255,0.45); width: 103px; }
  .range .head td { background: var(--blue-head); }
  .range .r1 td { background: var(--blue-1); }
  .range .r2 td { background: var(--blue-2); }
  .range .r3 td { background: var(--blue-3); }
  .caution { left: 38px; top: 422px; width: 570px; }
  .caution h2 { font-size: 15px; font-weight: 700; margin-bottom: 7px; }
  .drugs {
    position: absolute; left: 38px; top: 543px; width: 557px;
    border-collapse: collapse; font-size: 15px; line-height: 17.7px;
  }
  .drugs th {
    background: var(--purple); color: #fff; height: 33px; text-align: left;
    font-weight: 700; font-size: 14.5px; padding-left: 19px;
  }
  .drugs th + th { border-left: 1px solid rgba(255,255,255,0.5); }
  .drugs td { vertical-align: top; padding: 9px 12px 0 19px; }
  .drugs td.drug { border-left: 1px solid rgba(255,255,255,0.8); padding-left: 14px; }
  .drugs tr.cyan td { background: var(--cyan-row); }
  .drugs tr.lav td { background: var(--lavender-row); }
  .drugs .bullets li + li { margin-top: 11px; }
  .differential { left: 38px; top: 955px; width: 570px; }
  .differential h2 { font-size: 15px; font-weight: 700; }
  .diff-col { position: absolute; top: 28px; }
  .diff-col li { position: absolute; left: 0; white-space: nowrap; padding-left: 13px; }
  .diff-col li::before { left: 0; }
</style>
</head>
<body>
<main class="page">
  <header class="banner">
    <h1>Hypertension, Acute</h1>
    <p>Sustained high blood pressure refractory to treating<br>reversible causes</p>
  </header>

  <p class="block intro">In pediatrics, hypertension is almost always treated by addressing likely causes such as light anesthesia or measurement error:</p>

  <ul class="block bullets checks">
    <li style="top:0">Ensure correct BP cuff size:<br>cuff bladder width ~ 40% of<br>limb circumference</li>
    <li style="top:75px">Ensure arterial line transducer is<br>at level of heart</li>
    <li style="top:133px">Consider placing arterial line<br>if not&nbsp; already present</li>
  </ul>

  <table class="range">
    <tr><th class="title" colspan="3">Hypertensive Blood Pressure Range*</th></tr>
    <tr class="head"><td>Age (yr)</td><td>Systolic</td><td>Diastolic</td></tr>
    <tr class="r1"><td>newborn</td><td>&gt;97</td><td>&gt;70</td></tr>
    <tr class="r2"><td>1-3</td><td>&gt;105</td><td>&gt;61</td></tr>
    <tr class="r3"><td>4-12</td><td>&gt;113</td><td>&gt;86</td></tr>
  </table>

  <section class="block caution">
    <h2>*CAUTION</h2>
    <p>Anti-hypertensive drugs are almost never needed for routine pediatric cases. These medications are used almost exclusively for specialized cardiac, neurosurgical, or endocrine (pheochromocytoma) cases. Consult an expert&nbsp; before use.<br>Rule-out increased ICP.</p>
  </section>

  <table class="drugs">
    <colgroup><col style="width:181px"><col></colgroup>
    <tr><th>Action</th><th>Drug (IV Dosing)</th></tr>
    <tr class="cyan" style="height:66px">
      <td>Direct smooth muscle relaxation</td>
      <td class="drug"><ul class="bullets">
        <li>Sodium nitroprusside 0.5-10 MICROgrams/kg/min</li>
        <li>HydrALAZINE 0.1-0.2 mg/kg (adult dose 5-10 mg)</li>
      </ul></td>
    </tr>
    <tr class="lav" style="height:111px">
      <td style="padding-left:14px;padding-top:16px">β-Adrenergic<br>blockade</td>
      <td class="drug" style="padding-top:13px"><ul class="bullets purple">
        <li>Esmolol 100-500 MICROgrams/kg over 5 min, then 25-300 MICROgrams/kg/min</li>
        <li>Labetalol (also α effect) 0.2-1 mg/kg q 10 min; 0.4-3 mg/kg/hour (infusion)</li>
      </ul></td>
    </tr>
    <tr class="cyan" style="height:109px">
      <td style="padding-top:29px">Calcium channel<br>blockade</td>
      <td class="drug" style="padding-top:27px"><ul class="bullets">
        <li>niCARdapine 0.5-5 MICROgrams/kg/min</li>
        <li style="margin-top:20px">Clevidipine 0.5-3.5 MICROgrams/kg/min</li>
      </ul></td>
    </tr>
    <tr class="lav" style="height:66px">
      <td style="padding-top:23px">D1-dopamine agonist</td>
      <td class="drug" style="padding-top:23px"><ul class="bullets purple">
        <li>Fenoldopam 0.2-0.8 MICROgrams/kg/min</li>
      </ul></td>
    </tr>
  </table>

  <section class="block differential">
    <h2>CONSIDER DIFFERENTIAL (PARTIAL)</h2>
    <ul class="bullets diff-col" style="left:0">
      <li style="top:0">Light anesthesia (consider<br>vaporizer or infusion pump<br>empty or malfunctioning)</li>
      <li style="top:66px">Hypercarbia</li>
    </ul>
    <ul class="bullets diff-col" style="left:202px">
      <li style="top:1px">Hypoxemia</li>
      <li style="top:29px">Arterial line transducer too<br>low or BP cuff too small</li>
      <li style="top:74px">Withdrawal (EtOH or opioid)</li>
    </ul>
    <ul class="bullets diff-col" style="left:414px">
      <li style="top:2px">Thyroid Storm</li>
      <li style="top:29px">Pheochromocytoma</li>
      <li style="top:74px">Drug Error</li>
    </ul>
  </section>
</main>
</body>
</html>
```